Chocolate covered bananas

“I am starting a new venture making chocolate coated frozen bananas. At start up I intend to have 4 different types:
3 will be single bananas ( Dark Chocolate, Dark chocolate with sprinkles and Dark Chocolate & Almonds) sold in individual packets, 70MM(W) x 215mm(L)

The other will be Banana Pops (smaller pieces of banana) sold in a 500g bag and then packed in a 165mm(L) x 50mm(W) X 165mm(H) cardboard box

The packaging will need my logo the wording “Chocolate Coated Frozen Banana” and the slogan “Crunchy Sunny Snack” on it. A picture of a Banana and Chocolate (The chocolate can be on the banana, getting poured on it, or even beside it).
I would like the words “Zero Trans-fat” on both the packaging (3 variations) and the 500g container along with “Healthy Dessert Treat” on the Container.

I need the Ingredients and nutritional information on the back"

one version can be submitted within the Contest period, however the winner is required to provide all 4 versions as part of the project.

Good Luck

JUST A QUICK NOTE THE BANANAS WILL BE ON A ICE-CREAM STICK AND THE BANANA POPS WILL BE ON A POPSICLE STICK.

Here are a couple of examples from places in America (no competition to me I am in another country) I'm am looking for something similar in size. as the packets in merrily mangoes and the cartons in corals kiwis. http://www.merrily-mangoes.example/products.php and http://www.coralskiwis.example/our-products/ I hope this helps Regards Gareth.

Hi I am getting some great designs Most are dark brown (or chocolate ) in colour they look good however most ice cream packs are dark and I think in order for these to stand out they need to be brighter with the chocolate as a secondary colour. Regards Gareth.

Hi all great designs it will be very hard to pick. just a quick note I made a spelling mistake in my brief it is HEALTHY DESSERT TREAT (NOT DESERT) SORRY Regards Gareth.

I would like to thank everyone for there time and effort they have put in to my packaging design contest. I am meeting with the packaging company on Thursday and will have a decision Thursday night. Regards Gareth.

Target Market(s)

I plan to go down the track that these are a healthy tasty fun treat.
I will be using real Bananas and Real chocolate.

```html
<!DOCTYPE html>
<html lang="en">
<head>
<meta charset="utf-8">
<title>Chocolate Coated Frozen Banana Pops – Carton</title>
<link rel="stylesheet" href="https://fonts.googleapis.com/css2?family=Lobster&family=Arimo:wght@400;700&display=swap">
<style>
  :root {
    --stage: #ececec;
    --banana-yellow: #f8ec3c;
    --cocoa-dark: #241610;
    --cocoa: #6a4230;
    --cocoa-mid: #4a2c1f;
    --sunny-text: #f5e53a;
    --label-white: #ffffff;
    --ink: #111111;
  }
  * { box-sizing: border-box; margin: 0; padding: 0; }
  html, body {
    width: 1200px; height: 669px; overflow: hidden;
    background: var(--stage);
  }
  .carton {
    position: absolute; left: 315px; top: 100px;
    display: flex; width: 570px; height: 470px;
  }
  .front-panel {
    position: relative; width: 420px; height: 470px;
    background: var(--banana-yellow); overflow: hidden;
  }
  .side-panel {
    position: relative; width: 150px; height: 470px;
    background: var(--cocoa); overflow: hidden;
  }
  .display-type { font-family: "Lobster", cursive; color: var(--cocoa-dark); font-weight: 400; }

  .brand-mark {
    position: absolute; right: 18px; top: 16px;
    display: flex; flex-direction: column; align-items: center; gap: 4px;
  }
  .brand-mark__dot {
    width: 46px; height: 46px; border-radius: 50%;
    background: var(--cocoa-mid);
  }
  .brand-mark__name {
    font-family: "Lobster", cursive; font-size: 13px; color: var(--cocoa-dark);
  }

  .product-title {
    position: absolute; left: 18px; top: 34px;
    transform: rotate(-10deg); transform-origin: left top;
    line-height: 0.95;
  }
  .product-title__lead { display: block; font-size: 60px; }
  .product-title__rest { display: block; font-size: 32px; margin-left: 48px; }

  .claim {
    position: absolute; left: 22px; top: 258px;
    font-size: 24px; transform: rotate(-12deg); transform-origin: left top;
  }

  .hero-art {
    position: absolute; left: 195px; top: 130px; width: 185px; height: 280px;
    border-radius: 90px 90px 30px 30px;
    background: linear-gradient(170deg, #fbf6d8 0%, #f1e48a 45%, #8a5a3a 80%, #4a2c1f 100%);
  }

  .chocolate-band { position: absolute; left: 0; top: 0; width: 420px; height: 470px; }

  .fat-note {
    position: absolute; left: 52px; top: 312px;
    font-family: "Arimo", sans-serif; font-size: 12px; color: var(--ink);
  }

  .slogan {
    position: absolute; left: 14px; top: 370px;
    font-family: "Lobster", cursive; font-size: 19px; line-height: 1.05;
    color: var(--sunny-text); transform: rotate(-8deg);
  }

  .side-panel .brand-mark { right: auto; left: 50%; transform: translateX(-50%); top: 22px; }
  .side-panel .brand-mark__name { color: var(--sunny-text); }
  .side-panel .brand-mark__dot { background: var(--cocoa-dark); }

  .nutrition-facts {
    position: absolute; left: 10px; top: 110px; width: 130px;
    background: var(--label-white); border: 1px solid var(--ink);
    padding: 3px 4px; font-family: "Arimo", sans-serif; color: var(--ink);
    font-size: 6.2px; line-height: 1.25;
  }
  .nutrition-facts__title { font-size: 9.5px; font-weight: 700; line-height: 1.05; }
  .nutrition-facts__serving { border-bottom: 3px solid var(--ink); padding-bottom: 2px; }
  .nutrition-facts__row {
    display: flex; justify-content: space-between;
    border-bottom: 0.5px solid var(--ink); padding: 1px 0;
  }
  .nutrition-facts__row--sub { padding-left: 6px; }
  .nutrition-facts__row--bold { font-weight: 700; }
  .nutrition-facts__row--rule { border-bottom-width: 2px; }
</style>
</head>
<body>
  <div class="carton">
    <section class="front-panel">
      <div class="hero-art" role="img" aria-label="Peeled banana rising from a splash of melted chocolate"></div>

      <svg class="chocolate-band" viewBox="0 0 420 470" aria-hidden="true">
        <path d="M0 300 C18 310 30 338 60 346 C110 358 160 352 195 348 C260 360 330 392 420 380 L420 470 L0 470 Z" fill="var(--cocoa-dark)"/>
        <circle cx="192" cy="328" r="24" fill="var(--cocoa-dark)"/>
        <circle cx="222" cy="298" r="10" fill="var(--cocoa-dark)"/>
        <circle cx="160" cy="392" r="16" fill="var(--cocoa-dark)"/>
        <path d="M0 440 C110 420 240 430 420 442 L420 470 L0 470 Z" fill="var(--cocoa)"/>
      </svg>

      <div class="brand-mark">
        <span class="brand-mark__dot"></span>
        <span class="brand-mark__name">Gladly Groves</span>
      </div>

      <h1 class="product-title display-type">
        <span class="product-title__lead">Chocolate</span>
        <span class="product-title__rest">Coated Frozen</span>
        <span class="product-title__rest">Banana Pops</span>
      </h1>

      <p class="claim display-type">Healthy Desert Treat</p>
      <p class="fat-note">Zero Trans-fat</p>
      <p class="slogan">Crunchy<br>Sunny<br>Snack</p>
    </section>

    <aside class="side-panel">
      <div class="brand-mark">
        <span class="brand-mark__dot"></span>
        <span class="brand-mark__name">Gladly Groves</span>
      </div>

      <div class="nutrition-facts">
        <div class="nutrition-facts__title">Nutrition Facts<br>Valeur nutritive</div>
        <div class="nutrition-facts__serving">Per 1 large egg (53 g)<br>pour 1 oeuf gros (53 g)</div>
        <div class="nutrition-facts__row"><span>Amount<br>Teneur</span><span>% Daily Value<br>% valeur quotidienne</span></div>
        <div class="nutrition-facts__row nutrition-facts__row--bold"><span>Calories / Calories 70</span><span></span></div>
        <div class="nutrition-facts__row nutrition-facts__row--bold"><span>Fat / Lipides 5 g</span><span>8 %</span></div>
        <div class="nutrition-facts__row nutrition-facts__row--sub"><span>Saturated / Saturés 1.5 g</span><span>8 %</span></div>
        <div class="nutrition-facts__row nutrition-facts__row--sub"><span>+ Trans / Trans 0 g</span><span></span></div>
        <div class="nutrition-facts__row nutrition-facts__row--bold"><span>Cholesterol / Cholestérol 195 mg</span><span></span></div>
        <div class="nutrition-facts__row nutrition-facts__row--bold"><span>Sodium / Sodium 65 mg</span><span>3 %</span></div>
        <div class="nutrition-facts__row nutrition-facts__row--bold"><span>Carbohydrate / Glucides 1 g</span><span>1 %</span></div>
        <div class="nutrition-facts__row nutrition-facts__row--sub"><span>Fibre / Fibres 0 g</span><span>0 %</span></div>
        <div class="nutrition-facts__row nutrition-facts__row--sub"><span>Sugars / Sucres 0 g</span><span>0 %</span></div>
        <div class="nutrition-facts__row nutrition-facts__row--bold nutrition-facts__row--rule"><span>Protein / Protéines 6 g</span><span></span></div>
        <div class="nutrition-facts__row"><span>Vitamin A / Vitamine A</span><span>10 %</span></div>
        <div class="nutrition-facts__row"><span>Vitamin C / Vitamine C</span><span>0 %</span></div>
        <div class="nutrition-facts__row"><span>Calcium / Calcium</span><span>2 %</span></div>
        <div class="nutrition-facts__row"><span>Iron / Fer</span><span>6 %</span></div>
        <div class="nutrition-facts__row"><span>Vitamin E / Vitamine A</span><span>50%</span></div>
      </div>
    </aside>
  </div>
</body>
</html>
```